Start-up Cleaning Business Needs Professional Business Cards

Marisol's Butler Tidying, LLC, is a start-up business based in the Northern Virginia suburbs of Washington, DC. MBT provides cleaning and housekeeping services for homes and offices. We have three core values:

1. We are personal. We value knowing and being known by our customers and each other. If you want nameless, faceless service, you should choose another provider. We put "personal" at the front of the list, because it is most important to us; the design we choose will convey this value.

2. Like a hotel concierge, we are professional in attitude, posture, communication and processes.

3. Like a hotel concierge, we solve problems with a can-do attitude and never make excuses.

Our uniforms are khaki pants with pink polo shirts.

Our logo is attached. There are other symbols, not represented in our logo, that may convey our values well, such as a top hat and bow tie, magnifying glass, desk bell, etc.

Please include fields for an individual's name and title, office phone number, mobile phone number, email address and website address (www.marisolsbutlertidying-example.com).

Standard U.S. size: 2" x 3.5"
Updates

I should have mentioned that the purpose of all our advertising - business cards included - is to motivate potential customers to call or email to arrange a free in-home estimate.

```html
<!DOCTYPE html>
<html lang="en">
<head>
<meta charset="utf-8">
<title>Marisol's Butler Tidying – Business Cards</title>
<link rel="stylesheet" href="https://fonts.googleapis.com/css2?family=Montserrat:wght@300;400&display=swap">
<style>
  :root {
    --backdrop: #e4e2df;
    --card: #f1f1f0;
    --ink: #8b8b8b;
    --ink-dark: #5a5a5a;
    --pink: #d42a83;
    --pink-soft: #e27fb1;
    --sketch: #b8a9ad;
  }
  * { margin: 0; padding: 0; box-sizing: border-box; }
  html, body {
    width: 1200px; height: 900px; overflow: hidden;
    background: var(--backdrop);
    font-family: 'Montserrat', sans-serif;
    font-weight: 300;
    color: var(--ink);
  }
  .sheet {
    width: 1200px; height: 900px;
    display: flex; flex-direction: column;
    align-items: center; justify-content: center; gap: 40px;
  }
  .card {
    position: relative;
    width: 700px; height: 400px;
    background: var(--card);
    box-shadow: 0 2px 10px rgba(0,0,0,0.12);
    overflow: hidden;
  }

  /* Back side */
  .estimate-cloud {
    position: absolute; left: 70px; top: 125px;
    width: 300px; height: 170px;
  }
  .estimate-text {
    position: absolute; left: 70px; top: 125px;
    width: 300px; height: 170px;
    display: flex; align-items: center; justify-content: center;
    text-align: center;
    font-size: 24px; line-height: 1.25; letter-spacing: 0.5px;
    color: var(--ink-dark);
  }
  .peek-illustration {
    position: absolute; right: 40px; top: 0;
    width: 230px; height: 260px;
  }

  /* Front side */
  .contact {
    position: absolute; left: 60px; top: 70px;
    list-style: none;
  }
  .contact .name { font-size: 30px; color: var(--ink); letter-spacing: 0.5px; }
  .contact .title {
    font-size: 15px; letter-spacing: 1px; text-transform: uppercase;
    margin-bottom: 18px;
  }
  .contact .line { font-size: 17px; letter-spacing: 0.3px; }
  .contact .dot {
    width: 8px; height: 8px; border-radius: 50%;
    background: var(--pink);
    margin: 12px 0 12px 190px;
  }
  .mop-illustration {
    position: absolute; right: 40px; top: 30px;
    width: 200px; height: 200px;
  }
  .brand {
    position: absolute; right: 40px; top: 240px;
    text-align: right;
    font-size: 22px; font-weight: 300; color: var(--ink-dark);
    line-height: 1.2;
  }
</style>
</head>
<body>
<main class="sheet">

  <section class="card card-back">
    <svg class="estimate-cloud" viewBox="0 0 300 170" role="img" aria-label="Hand-painted pink cloud splash behind the call to action">
      <path fill="var(--pink)" d="M40 140 C5 135 5 95 30 85 C15 55 45 30 75 40 C85 10 135 5 150 30 C170 5 220 10 225 40 C260 30 295 55 280 85 C300 105 285 145 250 140 C235 165 190 165 170 150 C150 168 100 168 85 150 C70 162 45 158 40 140 Z"/>
    </svg>
    <p class="estimate-text">call or email<br>for an estimate</p>
    <div class="peek-illustration" role="img" aria-label="Sketched cleaning woman in pink peeking over the card edge">
      <svg width="230" height="260" viewBox="0 0 230 260">
        <defs>
          <linearGradient id="peekTone" x1="0" y1="0" x2="0" y2="1">
            <stop offset="0" stop-color="var(--sketch)" stop-opacity="0.55"/>
            <stop offset="1" stop-color="var(--pink-soft)" stop-opacity="0.55"/>
          </linearGradient>
        </defs>
        <rect width="230" height="260" rx="16" fill="url(#peekTone)"/>
      </svg>
    </div>
  </section>

  <section class="card card-front">
    <ul class="contact">
      <li class="name">Renata Alvarez</li>
      <li class="title">Operation Manager</li>
      <li class="line">T +55 21 80000147</li>
      <li class="dot" aria-hidden="true"></li>
      <li class="line">M +55 21 80000392</li>
      <li class="dot" aria-hidden="true"></li>
      <li class="line">alvarez@marisolsbutlertidying-example.com</li>
      <li class="dot" aria-hidden="true"></li>
      <li class="line">www.marisolsbutlertidying-example.com</li>
    </ul>
    <div class="mop-illustration" role="img" aria-label="Sketched cleaning woman in pink mopping the floor">
      <svg width="200" height="200" viewBox="0 0 200 200">
        <defs>
          <linearGradient id="mopTone" x1="0" y1="0" x2="0" y2="1">
            <stop offset="0" stop-color="var(--sketch)" stop-opacity="0.55"/>
            <stop offset="1" stop-color="var(--pink-soft)" stop-opacity="0.55"/>
          </linearGradient>
        </defs>
        <rect width="200" height="200" rx="16" fill="url(#mopTone)"/>
      </svg>
    </div>
    <p class="brand">Marisol's<br>Butler Tidying</p>
  </section>

</main>
</body>
</html>
```